Financial Service Company Need Business Card Design

This is a new startup company, first of its kind to offer this service. We facilitate the movement of deposit funds electronically between home buyers and real estate brokerages.Our customers are DOMIVANS®, real estate brokerages, and home buyers, we identify ourselves as a financial/technology company.
Not looking for anything too flashy. Just a clean design that shows the logo, contact info, etc. Company colors can be seen on attached logo, and 'coming soon page'
www.quorvanta.ca

```html
<!DOCTYPE html>
<html lang="en">
<head>
<meta charset="utf-8">
<title>Quorvanta — Business Card</title>
<link rel="stylesheet" href="https://fonts.googleapis.com/css2?family=Exo+2:wght@400;500;600&display=swap">
<style>
  :root {
    --brand-orange: #f0562a;
    --brand-orange-deep: #ee4a1e;
    --brand-grey: #55565b;
    --text-grey: #5a5b60;
    --paper: #ffffff;
    --stage: #ecebe8;
  }
  * { margin: 0; padding: 0; box-sizing: border-box; }
  html, body {
    width: 1200px;
    height: 1000px;
    overflow: hidden;
    background: var(--paper);
    font-family: "Exo 2", sans-serif;
  }
  .brand-header {
    height: 240px;
    display: flex;
    align-items: center;
    justify-content: center;
  }
  .brand-lockup {
    display: flex;
    align-items: center;
    gap: 16px;
  }
  .brand-square {
    width: 52px;
    height: 52px;
    background: var(--brand-orange);
  }
  .brand-name {
    font-weight: 500;
    font-size: 66px;
    color: var(--brand-grey);
    letter-spacing: -0.5px;
    line-height: 1;
  }
  .card-stage {
    height: 760px;
    background: var(--stage);
    display: flex;
    align-items: center;
    justify-content: center;
    gap: 40px;
  }
  .card {
    position: relative;
    width: 500px;
    height: 286px;
    background: var(--paper);
    box-shadow: 0 2px 6px rgba(0,0,0,0.12);
    overflow: hidden;
  }
  .card-back {
    display: flex;
    flex-direction: column;
    align-items: center;
    justify-content: center;
  }
  .card-back .brand-square { width: 30px; height: 30px; }
  .card-back .brand-name { font-size: 38px; }
  .card-back .brand-lockup { gap: 10px; }
  .card-url {
    margin-top: 6px;
    margin-left: 40px;
    font-size: 15px;
    letter-spacing: 0.5px;
    color: var(--brand-orange);
  }
  .card-front .front-lockup {
    position: absolute;
    top: 44px;
    left: 0;
    right: 0;
    display: flex;
    justify-content: center;
  }
  .card-front .brand-square { width: 30px; height: 30px; }
  .card-front .brand-name { font-size: 40px; }
  .card-front .brand-lockup { gap: 10px; }
  .name-band {
    position: absolute;
    left: 0;
    top: 138px;
    width: 100%;
    height: 52px;
  }
  .name-band svg { position: absolute; inset: 0; }
  .holder {
    position: absolute;
    left: 0;
    top: 6px;
    width: 420px;
    text-align: center;
    color: var(--paper);
  }
  .holder-name { font-size: 20px; font-weight: 500; line-height: 1.1; }
  .holder-title { font-size: 13px; font-weight: 500; }
  .contact {
    position: absolute;
    top: 204px;
    left: 0;
    width: 420px;
    text-align: center;
    font-size: 13px;
    line-height: 1.5;
    color: var(--text-grey);
    letter-spacing: 0.3px;
  }
</style>
</head>
<body>
  <header class="brand-header">
    <div class="brand-lockup">
      <span class="brand-square"></span>
      <span class="brand-name">Quorvanta</span>
    </div>
  </header>

  <main class="card-stage">
    <section class="card card-back">
      <div class="brand-lockup">
        <span class="brand-square"></span>
        <span class="brand-name">Quorvanta</span>
      </div>
      <p class="card-url">quorvanta.ca</p>
    </section>

    <section class="card card-front">
      <div class="front-lockup">
        <div class="brand-lockup">
          <span class="brand-square"></span>
          <span class="brand-name">Quorvanta</span>
        </div>
      </div>
      <div class="name-band">
        <svg width="500" height="52" viewBox="0 0 500 52">
          <rect x="0" y="0" width="500" height="52" fill="var(--brand-orange-deep)"/>
          <polygon points="400,0 416,0 448,52 432,52" fill="var(--paper)"/>
          <polygon points="430,0 446,0 478,52 462,52" fill="var(--paper)"/>
          <polygon points="460,0 500,0 500,12 468,12" fill="var(--brand-orange)"/>
        </svg>
        <div class="holder">
          <p class="holder-name">Your Name</p>
          <p class="holder-title">Title</p>
        </div>
      </div>
      <div class="contact">
        <p>M: (XXX) 555 1234</p>
        <p>name@domain.ca</p>
      </div>
    </section>
  </main>
</body>
</html>
```